BLUE FORGE (Business Card for Training Company)

Blue Forge is a training and consultancy company with a focus on executive protection and medical. I would like the card to be nice and sharp, not overdone and in black and red. I would also like it to highlight that it is "A Tavmont Company"

I would like it to be simple and highlight a few things.

1. Name
2. Title
3. Phone Number
4. Email

I would also like www.tavmontgroup.example/blue-forge to be on the card somewhere.

Target Market(s)

Security Companies

Industry/Entity Type

Security

Contact Information for Business Card

Blue Forge is a training and consultancy company with a focus on executive protection and medical. I would like the card to be nice and sharp, not overdone and in black and red. I would also like it to highlight that it is "A Tavmont Company" I would like it to be simple and highlight a few things. 1. Name 2. Title 3. Phone Number 4. Email I would also like www.tavmontgroup.example/blue-forge to be on the card somewhere.

Requirements
Must have
• A Tavmont Company listed on the card and the website
Nice to have
• Highlight Medical Training, Consultancy & Executive Protection Courses

```html
<!DOCTYPE html>
<html lang="en">
<head>
<meta charset="utf-8">
<title>Blue Forge – Business Card</title>
<link rel="stylesheet" href="https://fonts.googleapis.com/css2?family=Roboto:wght@400;500;700;900&display=swap">
<style>
  :root {
    --brand-red: #6d1014;
    --ink: #141414;
    --paper: #ffffff;
    --backdrop: #d9d9d9;
  }
  html, body {
    margin: 0;
    padding: 0;
    overflow: hidden;
  }
  .canvas {
    width: 1200px;
    height: 895px;
    background: var(--backdrop);
    position: relative;
    font-family: "Roboto", Arial, sans-serif;
    color: var(--ink);
  }
  .card {
    position: absolute;
    left: 260px;
    width: 680px;
    height: 388px;
    background: var(--paper);
    box-shadow: 0 6px 18px rgba(0,0,0,0.18);
  }
  .card--front { top: 40px; }
  .card--back  { top: 467px; }

  /* Front */
  .front-brand {
    position: absolute;
    top: 92px;
    left: 0;
    right: 0;
    text-align: center;
  }
  .wordmark {
    font-weight: 900;
    color: var(--brand-red);
    letter-spacing: 1px;
    line-height: 1;
    margin: 0;
  }
  .front-brand .wordmark { font-size: 68px; }
  .parent-line {
    display: inline-block;
    margin-top: 14px;
    padding: 5px 18px;
    font-size: 13px;
    font-weight: 500;
    letter-spacing: 6px;
    color: var(--brand-red);
    border-top: 2px solid var(--brand-red);
  }
  .tagline {
    position: absolute;
    bottom: 46px;
    left: 0;
    right: 0;
    text-align: center;
    font-size: 15px;
    font-weight: 700;
    letter-spacing: 0.3px;
  }

  /* Back */
  .contact {
    position: absolute;
    top: 110px;
    right: 345px;
    text-align: right;
  }
  .contact__name {
    font-size: 29px;
    font-weight: 700;
    color: var(--brand-red);
    margin: 0;
    letter-spacing: 0.5px;
  }
  .contact__title {
    font-size: 17px;
    margin: 2px 0 18px;
  }
  .contact__list {
    list-style: none;
    margin: 0;
    padding: 0;
    font-size: 17px;
    line-height: 1.35;
  }
  .contact__list li {
    display: flex;
    justify-content: flex-end;
    align-items: center;
    gap: 8px;
  }
  .contact__list svg {
    width: 13px;
    height: 13px;
    fill: var(--brand-red);
    flex: none;
  }
  .back-brand {
    position: absolute;
    top: 120px;
    left: 362px;
  }
  .back-brand .wordmark { font-size: 62px; }
</style>
</head>
<body>
<div class="canvas">

  <section class="card card--front">
    <div class="front-brand">
      <p class="wordmark">BLUE FORGE</p>
      <span class="parent-line">A TAVMONT COMPANY</span>
    </div>
    <p class="tagline">Medical Training, Consultancy &amp; Executive Protection Courses</p>
  </section>

  <section class="card card--back">
    <div class="contact">
      <h1 class="contact__name">DANIEL HARTLEY</h1>
      <p class="contact__title">Founder &amp; CEO</p>
      <ul class="contact__list">
        <li>+44 7700 900123
          <svg viewBox="0 0 24 24" aria-hidden="true"><path d="M6.6 10.8a15.1 15.1 0 0 0 6.6 6.6l2.2-2.2a1 1 0 0 1 1-.25 11.4 11.4 0 0 0 3.6.57 1 1 0 0 1 1 1V20a1 1 0 0 1-1 1A17 17 0 0 1 3 4a1 1 0 0 1 1-1h3.5a1 1 0 0 1 1 1c0 1.25.2 2.45.57 3.57a1 1 0 0 1-.25 1z"/></svg>
        </li>
        <li>d_hartley@mailbox.example
          <svg viewBox="0 0 24 24" aria-hidden="true"><path d="M2 5h20v14H2zm2 2v.5l8 5 8-5V7zm0 2.8V17h16V9.8l-8 5z"/></svg>
        </li>
        <li>tavmontgroup.example/blue-forge
          <svg viewBox="0 0 24 24" aria-hidden="true"><path d="M12 2a10 10 0 1 0 0 20 10 10 0 0 0 0-20zm6.9 6h-3a15.6 15.6 0 0 0-1.4-3.6A8 8 0 0 1 18.9 8zM12 4c.8 1.2 1.5 2.5 1.9 4h-3.8c.4-1.5 1.1-2.8 1.9-4zM4.3 14a8 8 0 0 1 0-4h3.4a16 16 0 0 0 0 4zm.8 2h3a15.6 15.6 0 0 0 1.4 3.6A8 8 0 0 1 5.1 16zm3-8h-3a8 8 0 0 1 4.4-3.6C8.9 5.5 8.4 6.7 8.1 8zM12 20c-.8-1.2-1.5-2.5-1.9-4h3.8c-.4 1.5-1.1 2.8-1.9 4zm2.3-6H9.7a14.6 14.6 0 0 1 0-4h4.6a14.6 14.6 0 0 1 0 4zm.2 5.6c.6-1.1 1.1-2.3 1.4-3.6h3a8 8 0 0 1-4.4 3.6zm1.8-5.6a16 16 0 0 0 0-4h3.4a8 8 0 0 1 0 4z"/></svg>
        </li>
      </ul>
    </div>
    <div class="back-brand">
      <p class="wordmark">BLUE FORGE</p>
    </div>
  </section>

</div>
</body>
</html>
```